Virtual Assistant/Online Marketing Business Card/Stationary

I need a professional but modern business card/stationary for my company in Dallas called Brivolo. Brivolo is a virtual assistant specializing in online marketing. I would like a unique design that stands out and makes my brand clear. Incorporating the logo is a must and have attached it to this brief.

Target Market(s)

small business owners & entrepreneurs, 35-65

Industry/Entity Type

Business

Contact Information for Business Card

Maren Tolk
marentolk@brivolo.biz
(555) 271-9064
brivolo.biz

Font styles to use
Sans Serif

Colors
f04a50
3176b5
9bcb3c

Requirements
Must have
• Colors that match the logo colors. Logo integration

```html
<!DOCTYPE html>
<html lang="en">
<head>
<meta charset="utf-8">
<title>Brivolo Business Card</title>
<link rel="stylesheet" href="https://fonts.googleapis.com/css2?family=Roboto:wght@400;500;700&display=swap">
<style>
  :root {
    --backdrop: #ffffff;
    --mount: #d3d4d6;
    --card-black: #060606;
    --card-glow: #2a2a2a;
    --paper: #eef2f4;
    --ink: #231f20;
    --white: #ffffff;
    --brand-red: #f04a50;
    --brand-green: #9bcb3c;
    --brand-blue: #3176b5;
    --stripe-red: #d2452f;
    --stripe-teal: #3aa6b1;
    --text-light: #f2f2f2;
  }
  * { box-sizing: border-box; margin: 0; padding: 0; }
  html, body {
    width: 1200px;
    height: 440px;
    overflow: hidden;
    background: var(--backdrop);
    font-family: "Roboto", Arial, sans-serif;
  }
  .canvas {
    position: relative;
    width: 1200px;
    height: 440px;
  }
  .mount {
    position: absolute;
    left: 10px;
    top: 41px;
    width: 1177px;
    height: 340px;
    background: var(--mount);
  }
  .card {
    position: absolute;
    top: 49px;
    width: 562px;
    height: 312px;
    overflow: hidden;
  }
  /* Front */
  .card--front {
    left: 18px;
    background:
      radial-gradient(ellipse 60% 55% at 50% 12%, var(--card-glow) 0%, rgba(6,6,6,0) 100%),
      var(--card-black);
  }
  .brand--front {
    position: absolute;
    left: 0;
    right: 0;
    top: 146px;
    display: flex;
    align-items: center;
    justify-content: center;
    gap: 14px;
  }
  .brand__dot {
    width: 30px;
    height: 30px;
    border-radius: 50%;
    background: var(--brand-red);
  }
  .brand__name {
    font-weight: 700;
    letter-spacing: -1px;
    line-height: 1;
  }
  .brand--front .brand__name {
    font-size: 68px;
    color: var(--text-light);
  }
  /* Back */
  .card--back {
    left: 614px;
    background:
      radial-gradient(ellipse 45% 50% at 45% 58%, #1e1e1e 0%, rgba(6,6,6,0) 100%),
      var(--card-black);
  }
  .card__header {
    position: absolute;
    left: 0;
    top: 0;
    width: 100%;
    height: 142px;
    background: var(--paper);
  }
  .brand--back {
    position: absolute;
    left: 28px;
    top: 68px;
  }
  .brand--back .brand__name {
    font-size: 42px;
    color: var(--ink);
  }
  .holder-name {
    position: absolute;
    right: 26px;
    top: 76px;
    font-size: 31px;
    color: var(--ink);
    text-transform: uppercase;
    letter-spacing: 0.3px;
    line-height: 1;
    font-weight: 400;
  }
  .holder-name__first { font-weight: 700; }
  .stripes {
    position: absolute;
    left: 0;
    top: 142px;
    width: 100%;
  }
  .stripe { height: 5px; }
  .stripe--green { background: var(--brand-green); }
  .stripe--red { background: var(--stripe-red); }
  .stripe--teal { background: var(--stripe-teal); }
  .contact-list {
    position: absolute;
    left: 167px;
    top: 166px;
    list-style: none;
  }
  .contact-item {
    display: flex;
    align-items: center;
    gap: 14px;
    height: 36px;
    margin-bottom: 13px;
    color: var(--text-light);
    font-size: 14.5px;
  }
  .contact-item:nth-child(3) { margin-top: -3px; }
  .contact-icon {
    width: 36px;
    height: 36px;
    border-radius: 50%;
    background: var(--white);
    display: flex;
    align-items: center;
    justify-content: center;
    flex: none;
  }
  .contact-icon svg { width: 20px; height: 20px; }
</style>
</head>
<body>
<div class="canvas">
  <div class="mount"></div>

  <section class="card card--front" aria-label="Card front">
    <div class="brand brand--front">
      <span class="brand__dot"></span>
      <span class="brand__name">Brivolo</span>
    </div>
  </section>

  <section class="card card--back" aria-label="Card back">
    <div class="card__header">
      <div class="brand brand--back">
        <span class="brand__name">Brivolo</span>
      </div>
      <h1 class="holder-name"><span class="holder-name__first">Maren</span> Tolk</h1>
    </div>
    <div class="stripes">
      <div class="stripe stripe--green"></div>
      <div class="stripe stripe--red"></div>
      <div class="stripe stripe--teal"></div>
    </div>
    <ul class="contact-list">
      <li class="contact-item">
        <span class="contact-icon">
          <svg viewBox="0 0 24 24" aria-hidden="true">
            <rect x="2.5" y="5.5" width="19" height="13" fill="none" stroke="#111" stroke-width="2"/>
            <path d="M3 6.5 L12 13 L21 6.5" fill="none" stroke="#111" stroke-width="2"/>
          </svg>
        </span>
        <span class="contact-text">marentolk@brivolo.biz</span>
      </li>
      <li class="contact-item">
        <span class="contact-icon">
          <svg viewBox="0 0 24 24" aria-hidden="true">
            <path fill="#111" d="M6.6 10.8c1.4 2.8 3.8 5.1 6.6 6.6l2.2-2.2c.3-.3.7-.4 1-.2 1.1.4 2.3.6 3.6.6.6 0 1 .4 1 1V20c0 .6-.4 1-1 1C10.6 21 3 13.4 3 4c0-.6.4-1 1-1h3.5c.6 0 1 .4 1 1 0 1.3.2 2.5.6 3.6.1.3 0 .7-.2 1L6.6 10.8z"/>
          </svg>
        </span>
        <span class="contact-text">(555) 271-9064</span>
      </li>
      <li class="contact-item">
        <span class="contact-icon">
          <svg viewBox="0 0 24 24" aria-hidden="true">
            <circle cx="12" cy="12" r="9" fill="none" stroke="#111" stroke-width="2"/>
            <ellipse cx="12" cy="12" rx="4" ry="9" fill="none" stroke="#111" stroke-width="1.6"/>
            <path d="M3.5 9h17M3.5 15h17" stroke="#111" stroke-width="1.6"/>
          </svg>
        </span>
        <span class="contact-text">brivolo.biz</span>
      </li>
    </ul>
  </section>
</div>
</body>
</html>
```